Lumen Hall of Music Website Design

Lumen Hall of Music would like to have a website designed. They are a new business similar to Quorvale (https://quorvaletunes.example).

We prefer using Adobe Fonts throughout the design. Kepler was used for the logo. Lorem Ipsum is fine to use except for headers.

Please keep track of any images/icons that are used in your design. We plan on purchasing the images used in the winning design.

Target Market(s)

Children age 10 - 18

Number of Pages Required

1 page

Font styles to use
Sans Serif

Colors
0054AA
0677BA
7BADD7
CADEEF
E8F1F8

```html
<!DOCTYPE html>
<html lang="en">
<head>
<meta charset="utf-8">
<title>Lumen Hall of Music</title>
<link href="https://fonts.googleapis.com/css2?family=Source+Serif+4:wght@400;600;700&family=Roboto:wght@400&display=swap" rel="stylesheet">
<style>
:root{
  --blue:#0054AA;--blue2:#0677BA;--mid:#7BADD7;--pale:#CADEEF;--mist:#E8F1F8;
  --ink:#2b2b2b;--white:#fff;
}
*{box-sizing:border-box;margin:0;padding:0}
html,body{width:1200px;height:4155px;overflow:hidden}
body{position:relative;font-family:"Source Serif 4",Georgia,serif;color:var(--ink);background:var(--white)}
.abs{position:absolute}
.title{font-weight:700;color:var(--blue);letter-spacing:1.5px;text-transform:uppercase;font-size:31px;text-align:center;width:1200px;left:0}
.btn{position:absolute;background:var(--mid);color:#fff;font-size:12px;letter-spacing:1px;text-transform:uppercase;display:flex;align-items:center;justify-content:center;border-radius:2px}
.photo{position:absolute;border-radius:4px}
.logo-box{position:absolute;left:126px;top:0;width:158px;height:150px;background:#fff;border-left:6px solid var(--blue2);box-shadow:0 2px 6px rgba(0,0,0,.15);display:flex;flex-direction:column;align-items:center;justify-content:center;gap:8px;z-index:3}
.logo-mark{width:46px;height:46px;border-radius:50%;background:var(--blue)}
.logo-name{color:var(--blue);font-weight:700;font-size:22px;letter-spacing:1px}
.logo-sub{font-size:9px;color:var(--blue);letter-spacing:.5px;text-transform:uppercase}
.nav{position:absolute;top:60px;left:402px;display:flex;gap:33px;font-size:13px;color:var(--blue);letter-spacing:.6px}
.tool{position:absolute;top:15px;height:29px;border:1px solid var(--pale);display:flex;align-items:center;justify-content:center;font-size:11px;color:var(--blue);border-radius:2px}
.card{position:absolute;width:428px;height:125px;background:#fff;border-radius:4px;box-shadow:0 1px 4px rgba(0,0,0,.06)}
.card .photo{left:7px;top:7px;width:198px;height:110px}
.card h3{position:absolute;left:228px;top:38px;font-size:16px;color:var(--blue);letter-spacing:1px;text-transform:uppercase;line-height:1.3;width:190px}
.card p{position:absolute;left:228px;font-size:14px;line-height:1.45;width:190px}
.teacher{position:absolute;top:1955px;width:207px;text-align:center}
.teacher .frame{width:207px;height:197px;border:1px solid var(--pale);border-radius:4px;background:#fff;padding:8px}
.teacher .frame div{width:100%;height:100%}
.teacher.active .frame{border:3px solid var(--blue)}
.teacher h4{margin-top:12px;font-size:17px;color:var(--blue2);font-weight:600}
.teacher small{display:block;font-size:12px;margin-top:2px}
.socials{display:flex;justify-content:center;gap:20px;margin-top:10px}
.socials i{width:9px;height:9px;border-radius:50%;background:var(--mid);display:block}
.post{position:absolute;top:3026px;width:297px}
.post .photo{position:static;height:171px;border-radius:2px}
.post p{font-size:13px;line-height:1.6;margin-top:20px}
.meta{display:flex;gap:20px;font-size:12px;margin-top:14px;align-items:center}
.meta span{display:flex;align-items:center;gap:6px}
.info{position:absolute;left:185px;display:flex;gap:18px;align-items:flex-start}
.info .ic{width:52px;height:52px;border-radius:50%;background:var(--blue);display:flex;align-items:center;justify-content:center;flex:none}
.info b{display:block;font-size:12px;color:var(--blue);letter-spacing:1px;margin-top:4px}
.info span{font-size:14px;line-height:1.4}
.field{position:absolute;background:#fff;border:1px solid var(--pale);font-size:12px;color:#999;padding:10px 16px;display:flex;gap:8px;font-family:Roboto,Arial,sans-serif}
.partner{position:absolute;top:4023px;height:54px;background:var(--pale);border-radius:4px}
</style>
</head>
<body>

<header>
  <div class="logo-box"><div class="logo-mark"></div><div class="logo-name">LUMEN</div><div class="logo-sub">Hall of Music</div></div>
  <div class="tool" style="left:753px;width:29px"><svg width="13" height="13" viewBox="0 0 14 14" fill="none" stroke="#0054AA" stroke-width="1.6"><circle cx="6" cy="6" r="4.5"/><path d="M9.5 9.5 13 13"/></svg></div>
  <div class="tool" style="left:793px;width:29px"><svg width="13" height="13" viewBox="0 0 14 14" fill="none" stroke="#0054AA" stroke-width="1.4"><circle cx="7" cy="4.5" r="3"/><path d="M1.5 13c0-3 2.5-5 5.5-5s5.5 2 5.5 5"/></svg></div>
  <div class="tool" style="left:832px;width:52px">EN ▾</div>
  <div class="btn" style="left:893px;top:15px;width:91px;height:29px;background:var(--blue)">Register</div>
  <div class="btn" style="left:993px;top:15px;width:81px;height:29px">Donate</div>
  <nav class="nav"><span>OUR PROGRAMS</span><span>ABOUT US</span><span>OUR IMPACT</span><span>SUPPORT QUORVALE</span><span>STUDENT RESOURCES</span></nav>
</header>

<section>
  <div class="abs" role="img" aria-label="Photo of hands playing a violin, in deep blue tones" style="left:0;top:89px;width:1200px;height:556px;background:linear-gradient(100deg,#1c3566,#2c4f86 55%,#6a5a66)"></div>
  <svg class="abs" style="left:0;top:500px" width="1200" height="150"><polygon points="0,145 1200,20 1200,150 0,150" fill="#fff"/><polygon points="700,60 1200,10 1200,110" fill="#CADEEF"/></svg>
  <div class="abs" style="left:0;top:285px;width:1200px;text-align:center;color:#fff;font-size:26px;letter-spacing:3px">WELCOME TO</div>
  <div class="abs" style="left:0;top:318px;width:1200px;text-align:center;color:#fff;font-size:44px;font-weight:600;letter-spacing:2px">OUR MUSIC SCHOOL</div>
  <div class="btn" style="left:537px;top:384px;width:126px;height:32px;background:var(--blue)">Contact Us</div>
</section>

<section>
  <h2 class="abs" style="left:126px;top:725px;font-size:31px;color:var(--blue);letter-spacing:1.5px">ABOUT US</h2>
  <p class="abs" style="left:126px;top:782px;width:440px;font-size:17px;color:var(--blue2);line-height:1.45">Lorem Ipsum is simply dummy text of the printing and typesetting industry.</p>
  <p class="abs" style="left:126px;top:838px;width:440px;font-size:13px;line-height:1.75">Lorem Ipsum has been the industry's standard dummy text ever since the 1500s, when an unknown printer took a galley of type and scrambled it to make a type specimen book. It has survived not only five centuries, but also the leap into electronic...</p>
  <div class="btn" style="left:126px;top:952px;width:119px;height:30px">Read More</div>
  <div class="photo" role="img" aria-label="Photo of a group of school children holding instruments" style="left:665px;top:697px;width:406px;height:322px;background:linear-gradient(135deg,#8ea6c4,#5a6f93 60%,#c79a6a);box-shadow:0 2px 8px rgba(0,0,0,.2)"></div>
</section>

<section>
  <svg class="abs" style="left:0;top:1085px" width="1200" height="740"><polygon points="0,70 1200,20 1200,740 0,740" fill="#E8F1F8"/><polygon points="0,0 340,55 0,70" fill="#CADEEF"/></svg>
  <h2 class="title abs" style="top:1216px">Our Programs</h2>
  <div class="card" style="left:161px;top:1287px"><div class="photo" role="img" aria-label="Photo of young children in a classroom circle" style="background:linear-gradient(135deg,#e4c9a0,#b7a58c)"></div><h3>Early Childhood</h3><p style="top:64px">Newborns – 8 years</p></div>
  <div class="card" style="left:613px;top:1287px"><div class="photo" role="img" aria-label="Photo of children in costumes at summer camp" style="background:linear-gradient(135deg,#c94a3c,#e8d3c2)"></div><h3>Summer Camps</h3><p style="top:64px">All ages. By experience.</p></div>
  <div class="card" style="left:161px;top:1427px"><div class="photo" role="img" aria-label="Photo of a private piano lesson" style="background:linear-gradient(135deg,#e9e9e6,#8b7769)"></div><h3>Private Lessons</h3><p style="top:64px">Ages 4+</p>
    <div class="abs" style="left:391px;top:85px;width:28px;height:28px;border-radius:5px;background:var(--blue2)"><svg width="28" height="28" viewBox="0 0 28 28" fill="none" stroke="#fff" stroke-width="2"><path d="M8 14h12M15 9l5 5-5 5"/></svg></div></div>
  <div class="card" style="left:613px;top:1427px"><div class="photo" role="img" aria-label="Photo of a student string orchestra" style="background:linear-gradient(135deg,#3c3a36,#8a7a66)"></div><h3 style="top:28px">Elena R. Whitcombe Conservatory</h3><p style="top:74px">All ages. All tuition-free.</p></div>
  <div class="card" style="left:161px;top:1568px"><div class="photo" role="img" aria-label="Photo of a group guitar class outdoors" style="background:linear-gradient(135deg,#9bb36c,#d9c4a4)"></div><h3>Group Classes</h3><p style="top:64px">Ages 6+</p></div>
  <div class="card" style="left:613px;top:1568px"><div class="photo" role="img" aria-label="Photo of children playing brass instruments" style="background:linear-gradient(135deg,#6a7fa0,#c49a5c)"></div><h3 style="top:22px">Quorvale Music in Communities</h3><p style="top:68px">School-age children across Chicago.</p></div>
  <svg class="abs" style="left:0;top:1775px" width="1200" height="60"><polygon points="850,10 1200,0 1200,55" fill="#CADEEF"/></svg>
</section>

<section>
  <h2 class="title abs" style="top:1885px">Our Teachers</h2>
  <div class="teacher" style="left:132px"><div class="frame"><div role="img" aria-label="Portrait of violin teacher" style="background:linear-gradient(135deg,#ddd,#7a4a3a)"></div></div><h4>Dana Whitfield</h4><small>Violin teacher</small><div class="socials"><i></i><i></i><i></i></div></div>
  <div class="teacher" style="left:369px"><div class="frame"><div role="img" aria-label="Portrait of drums teacher" style="background:linear-gradient(135deg,#e6e6e6,#9a8678)"></div></div><h4>Owen Tarrant</h4><small>Drums teacher</small><div class="socials"><i></i><i></i><i></i></div></div>
  <div class="teacher active" style="left:606px"><div class="frame"><div role="img" aria-label="Portrait of guitar teacher" style="background:linear-gradient(135deg,#d8c6a4,#8a6a48)"></div></div><h4>Mira Castellan</h4><small>Guitar teacher</small><div class="socials"><i></i><i></i><i></i></div></div>
  <div class="teacher" style="left:844px"><div class="frame"><div role="img" aria-label="Portrait of vocal teacher" style="background:linear-gradient(135deg,#3a3a3a,#b59b84)"></div></div><h4>Lena Voskuil</h4><small>Vocal teacher</small><div class="socials"><i></i><i></i><i></i></div></div>
  <div class="btn" style="left:548px;top:2258px;width:104px;height:31px">View All</div>
</section>

<section>
  <div class="abs" role="img" aria-label="Photo of smiling children in a classroom, darkened" style="left:0;top:2350px;width:1200px;height:560px;background:linear-gradient(110deg,#5a4a3a,#3a3530 50%,#6a6a70)"></div>
  <svg class="abs" style="left:0;top:2345px" width="1200" height="570"><polygon points="0,0 1200,0 1200,18 0,70" fill="#fff"/><polygon points="0,0 480,45 0,70" fill="#CADEEF"/><polygon points="0,555 1200,480 1200,570 0,570" fill="#fff"/></svg>
  <div class="abs" style="left:305px;top:2453px;width:590px;height:349px;background:#fff;border-radius:4px;text-align:center">
    <h2 style="margin-top:38px;font-size:31px;color:var(--blue);letter-spacing:1.5px">TESTIMONIALS</h2>
    <svg style="margin-top:18px" width="50" height="50" viewBox="0 0 50 50"><circle cx="25" cy="25" r="23" fill="none" stroke="#0054AA" stroke-width="2"/><text x="25" y="34" text-anchor="middle" font-size="26" font-weight="700" fill="#0054AA" font-family="Georgia,serif">“</text></svg>
    <p style="margin:22px auto 0;width:440px;font-size:13px;line-height:1.6">Lorem Ipsum is simply dummy text of the printing and typesetting industry. Lorem Ipsum has been the industry's standard dummy text ever since...</p>
    <div style="margin-top:26px;font-size:11px;display:flex;justify-content:center;gap:16px"><span>▣ 17 Jan, 2023</span><span style="color:#ccc">|</span><span style="color:var(--blue2)">Rafael Ondine</span></div>
    <div style="margin-top:30px;display:flex;justify-content:center;gap:8px;align-items:center"><i style="width:8px;height:8px;border:1px solid #999;border-radius:50%"></i><i style="width:10px;height:10px;background:var(--blue2);border-radius:50%"></i><i style="width:8px;height:8px;border:1px solid #999;border-radius:50%"></i></div>
  </div>
</section>

<section>
  <h2 class="title abs" style="top:2956px">Our Blogs</h2>
  <div class="post" style="left:126px"><div class="photo" role="img" aria-label="Photo of students with instruments" style="background:linear-gradient(135deg,#8ea6c4,#b88a60)"></div><p>Lorem Ipsum is simply dummy text of the printing and typesetting...</p><div class="meta"><span>▣ 17 Jan, 2023</span><span>→ Read More</span></div></div>
  <div class="post" style="left:452px"><div class="photo" role="img" aria-label="Photo of a teacher with children playing guitar" style="background:linear-gradient(135deg,#9bb36c,#d9c4a4)"></div><p>Lorem Ipsum is simply dummy text of the printing and typesetting...</p><div class="meta"><span>▣ 17 Jan, 2023</span><span>→ Read More</span></div></div>
  <div class="post" style="left:777px"><div class="photo" role="img" aria-label="Photo of children playing trumpets" style="background:linear-gradient(135deg,#6a7fa0,#c49a5c)"></div><p>Lorem Ipsum is simply dummy text of the printing and typesetting...</p><div class="meta"><span>▣ 17 Jan, 2023</span><span style="color:var(--blue);text-decoration:underline">→ Read More</span></div></div>
  <div class="btn" style="left:548px;top:3323px;width:104px;height:31px">View All</div>
</section>

<section>
  <svg class="abs" style="left:0;top:3408px" width="1200" height="570"><polygon points="0,0 1200,75 1200,570 0,570" fill="#E8F1F8"/><polygon points="0,0 330,70 0,85" fill="#CADEEF"/></svg>
  <h2 class="title abs" style="top:3545px;line-height:1.3">Have a question or<br>need more information?</h2>
  <div class="info" style="top:3662px"><div class="ic"><svg width="20" height="22" viewBox="0 0 20 22" fill="none" stroke="#fff" stroke-width="1.6"><path d="M10 21s7-7 7-12a7 7 0 0 0-14 0c0 5 7 12 7 12z"/><circle cx="10" cy="9" r="2.5"/></svg></div><div><b>LOCATION</b><span>Lorem ipsum, Fairview,<br>OR 97014, USA</span></div></div>
  <div class="info" style="top:3745px"><div class="ic"><svg width="20" height="20" viewBox="0 0 24 24" fill="none" stroke="#fff" stroke-width="1.8"><path d="M5 3h4l2 5-2.5 1.5a11 11 0 0 0 6 6L16 13l5 2v4a2 2 0 0 1-2 2A17 17 0 0 1 3 5a2 2 0 0 1 2-2z"/></svg></div><div><b>CALL US</b><span>(555)010-4567</span></div></div>
  <div class="info" style="top:3825px"><div class="ic"><svg width="20" height="16" viewBox="0 0 20 16" fill="none" stroke="#fff" stroke-width="1.6"><rect x="1" y="1" width="18" height="14" rx="1"/><path d="M1 2l9 7 9-7"/></svg></div><div><b>EMAIL</b><span>info@lumenhall.example</span></div></div>
  <div class="field" style="left:465px;top:3665px;width:265px;height:32px">◯ First Name</div>
  <div class="field" style="left:748px;top:3665px;width:265px;height:32px">◯ Last Name</div>
  <div class="field" style="left:465px;top:3710px;width:265px;height:32px">✉ Email</div>
  <div class="field" style="left:748px;top:3710px;width:265px;height:32px">☏ Phone</div>
  <div class="field" style="left:465px;top:3757px;width:548px;height:110px">▢ How can we help?</div>
  <div class="btn" style="left:463px;top:3887px;width:93px;height:32px">Submit</div>
</section>

<footer>
  <div class="partner" style="left:404px;width:128px"></div>
  <div class="partner" style="left:594px;width:138px"></div>
  <div class="partner" style="left:803px;width:70px"></div>
  <div class="partner" style="left:928px;width:130px"></div>
  <div class="abs" style="left:0;top:4110px;width:1200px;height:45px;background:var(--blue)"></div>
  <div class="logo-box" style="top:3998px;height:157px;border-left:none;box-shadow:none"><div class="logo-mark"></div><div class="logo-name">LUMEN</div><div class="logo-sub">Hall of Music</div></div>
  <div class="abs" style="left:415px;top:4124px;color:#fff;font-size:13px;font-family:Roboto,Arial,sans-serif">Copyright © 2023 Lumen Hall of Music . All Rights Reserved</div>
  <div class="abs" style="left:928px;top:4117px;display:flex;gap:9px"><i style="width:30px;height:30px;border-radius:50%;background:var(--mid);display:block"></i><i style="width:30px;height:30px;border-radius:50%;background:#fff;display:block"></i><i style="width:30px;height:30px;border-radius:50%;background:var(--mid);display:block"></i><i style="width:30px;height:30px;border-radius:50%;background:var(--mid);display:block"></i></div>
</footer>

</body>
</html>
```